BuildLinkHub.com Full Stationery Design

Business Card will have all info on it. Letterhead will not have name, title or mobile number. Keep general feeling very clean, using colors from the logo as accents.
Name:Dale Morrisette
Title:President
Phone: 1-800-555-0142
Cell: 306-555-0179
email: dale@buildlinkhub.example
website: www.buildlinkhub.example
Address:
PO Box 872
Elmridge, ER
S0J2T0

Target Market(s)

Construction Business owners

Industry/Entity Type

Business

Contact Information for Business Card

Name:Dale Morrisette
Title:President
Phone: 1-800-555-0142
Cell: 306-555-0179
Address:
PO Box 872
Elmridge, ER
S0J2T0

Font styles to use
Sans Serif

Requirements
Must have
• Clean look
Should not have
• Images or cartoon type characters or tools

```html
<!DOCTYPE html>
<html lang="en">
<head>
<meta charset="utf-8">
<title>BuildLinkHub.com Stationery</title>
<link href="https://fonts.googleapis.com/css2?family=Source+Sans+3:wght@400;500;600&family=Open+Sans:wght@400;600&display=swap" rel="stylesheet">
<style>
  :root {
    --backdrop: #5e6571;
    --paper: #ffffff;
    --ink: #3d3f44;
    --ink-soft: #66686e;
    --accent: #d9482b;
    --line-grey: #c9c9cc;
  }
  * { box-sizing: border-box; margin: 0; padding: 0; }
  html, body { width: 1200px; height: 1200px; overflow: hidden; }
  body {
    background: var(--backdrop);
    position: relative;
    font-family: "Source Sans 3", sans-serif;
    color: var(--ink);
  }
  .sheet { position: absolute; background: var(--paper); overflow: hidden; }

  .pattern-area {
    position: absolute;
    background: linear-gradient(135deg, #f4f4f6 0%, #fbf1ee 55%, rgba(255,255,255,0) 100%);
  }

  .brand { position: absolute; display: flex; align-items: center; gap: 8px; }
  .brand-mark { background: var(--accent); flex: none; }
  .brand-name { font-family: "Source Sans 3", sans-serif; font-weight: 500; color: var(--ink); white-space: nowrap; }

  /* Letterhead */
  .letterhead { left: 48px; top: 189px; width: 542px; height: 811px; }
  .letterhead .pattern-area { left: 0; top: 0; width: 312px; height: 262px; }
  .letterhead .brand { left: 122px; top: 140px; }
  .letterhead .brand-mark { width: 30px; height: 30px; }
  .letterhead .brand-name { font-size: 17px; }
  .letter-body { position: absolute; left: 85px; top: 266px; width: 373px; font-size: 10px; line-height: 16.3px; text-align: justify; color: var(--ink); }
  .letter-body p + p { margin-top: 16.3px; }
  .signature { position: absolute; left: 361px; top: 608px; }
  .signature-name { font-size: 14px; color: var(--ink); }
  .signature-title { font-size: 8px; margin-top: 6px; color: var(--ink-soft); }
  .footer { position: absolute; text-align: right; font-family: "Open Sans", sans-serif; letter-spacing: 0.08em; }
  .footer .web { color: var(--accent); }
  .footer .post { color: var(--ink-soft); }
  .footer b { font-weight: 600; }
  .letterhead .footer { right: 38px; top: 756px; font-size: 7.6px; line-height: 12px; }

  /* Business cards */
  .card { top: 372px; width: 219px; height: 145px; }
  .card-front { left: 628px; }
  .card-back { left: 862px; width: 220px; }
  .card-square { position: absolute; left: 15px; top: 28px; width: 24px; height: 24px; border: 1px solid var(--line-grey); }
  .card-person { position: absolute; left: 46px; top: 34px; font-family: "Open Sans", sans-serif; letter-spacing: 0.1em; color: var(--ink); }
  .card-person .name { font-size: 8px; text-transform: uppercase; }
  .card-person .role { font-size: 8px; margin-top: 3px; }
  .card-contact { position: absolute; left: 15px; top: 70px; font-family: "Open Sans", sans-serif; font-size: 6.5px; line-height: 10px; letter-spacing: 0.06em; color: var(--ink); }
  .card-contact b { font-weight: 600; }
  .card-divider { position: absolute; left: 148px; top: 72px; width: 1px; height: 38px; background: var(--accent); opacity: 0.6; }
  .card-address { position: absolute; left: 154px; top: 77px; font-family: "Open Sans", sans-serif; font-size: 6.5px; line-height: 10.5px; letter-spacing: 0.08em; color: var(--accent); }
  .card-back .pattern-area { inset: 0; background: linear-gradient(135deg, #f6f6f7 0%, #ffffff 45%, #fcf1ed 100%); }
  .card-back .brand { left: 55px; top: 64px; gap: 6px; }
  .card-back .brand-mark { width: 20px; height: 20px; }
  .card-back .brand-name { font-size: 12px; }

  /* Envelope */
  .envelope { left: 626px; top: 569px; width: 530px; height: 264px; }
  .envelope .pattern-area { left: 0; top: 0; width: 290px; height: 250px; }
  .envelope .brand { left: 112px; top: 134px; }
  .envelope .brand-mark { width: 28px; height: 28px; }
  .envelope .brand-name { font-size: 14px; }
  .envelope .footer { right: 23px; top: 221px; font-size: 6px; line-height: 10px; }
</style>
</head>
<body>

<section class="sheet letterhead">
  <div class="pattern-area" role="img" aria-label="Faint isometric line pattern in grey and rose"></div>
  <div class="brand">
    <span class="brand-mark"></span>
    <span class="brand-name">BuildLinkHub.com</span>
  </div>
  <div class="letter-body">
    <p>Lorem ipsum dolor sit amet, consectetur adipiscing elit. Donec orci purus, luctus vitae dignissim eu, iaculis sed purus. Vivamus faucibus, ipsum nec aliquet viverra, leo mauris condimentum ligula, sit amet sagittis enim ligula quis arcu. Nam egestas tortor id nisi porttitor mattis. In tortor ante, ultricies in suscipit a, tempus non massa. Vivamus et auctor mi. Fusce vel massa nulla. Phasellus nec eros mauris, et scelerisque orci. Donec malesuada orci vitae nulla accumsan porta a id massa. Quisque accumsan iaculis magna sit amet fringilla. Maecenas consequat, magna eget tincidunt semper, odio nibh rutrum mi, id feugiat ante nisi eu risus. Vestibulum nunc orci, rhoncus a placerat in, ultricies in mi. Cras mattis varius eros, vel fringilla nisi suscipit eget.</p>
    <p>Quisque scelerisque sagittis nulla at porttitor. Mauris a justo et tellus interdum tristique. Sed id augue vitae urna euismod commodo aliquet a quam. Pellentesque arcu velit, cursus et malesuada ut, consequat et diam. Nullam erat sem, rhoncus id ullamcorper vitae, rhoncus et arcu. In ultricies ultricies nulla, ut rutrum nisi iaculis at. Donec eu magna a metus ornare faucibus. Fusce aliquet faucibus ultricies. Morbi semper, est id tincidunt gravida, sem arcu adipiscing lacus, ac bibendum nulla leo eu purus. Quisque nec diam sed risus consectetur a ccumsan quis quis nibh. Vestibulum id purus lorem.</p>
  </div>
  <div class="signature">
    <div class="signature-name">Colin Barrett</div>
    <div class="signature-title">Co-Founder &amp; CEO</div>
  </div>
  <div class="footer">
    <div class="web">www.buildlinkhub.example</div>
    <div class="post">PO Box 872, Elmridge, ER S0J2T0 &nbsp;&nbsp; <b>P:</b> 1-800-555-0142</div>
  </div>
</section>

<section class="sheet card card-front">
  <span class="card-square"></span>
  <div class="card-person">
    <div class="name">Dale Morrisette</div>
    <div class="role">President</div>
  </div>
  <div class="card-contact">
    <div><b>P:</b> 1-800-555-0142</div>
    <div><b>C:</b> 306-555-0179</div>
    <div>www.buildlinkhub.example</div>
    <div>dale@buildlinkhub.example</div>
  </div>
  <span class="card-divider"></span>
  <div class="card-address">
    <div>PO Box 872</div>
    <div>Elmridge, ER</div>
    <div>S0J2T0</div>
  </div>
</section>

<section class="sheet card card-back">
  <div class="pattern-area" role="img" aria-label="Faint large isometric line pattern"></div>
  <div class="brand">
    <span class="brand-mark"></span>
    <span class="brand-name">BuildLinkHub.com</span>
  </div>
</section>

<section class="sheet envelope">
  <div class="pattern-area" role="img" aria-label="Faint isometric line pattern in grey and rose"></div>
  <div class="brand">
    <span class="brand-mark"></span>
    <span class="brand-name">BuildLinkHub.com</span>
  </div>
  <div class="footer">
    <div class="web">www.buildlinkhub.example</div>
    <div class="post">PO Box 872, Elmridge, ER S0J2T0 &nbsp;&nbsp; <b>P:</b> 1-800-555-0142</div>
  </div>
</section>

</body>
</html>
```